Visitenkarten-Design für Kfz-Werkstatt von Frauen für Frauen
Zielgruppe
Kfz-Werkstatt von Frauen für Frauen
Aufgabenstellung
Die Farben des Logos sollen sich in der Visitenkarte wieder spiegeln. Darf sehr feminin gehalten werden!
Infos auf der Visistenkarte:

```html
<!DOCTYPE html>
<html lang="de">
<head>
<meta charset="utf-8">
<title>Velmarin Visitenkarte</title>
<link rel="stylesheet" href="https://fonts.googleapis.com/css2?family=Montserrat:wght@700&family=Open+Sans:wght@400&display=swap">
<style>
  :root {
    --pink: #ee1a6b;
    --grey: #6b6b6b;
    --ink: #2b2b2b;
    --paper: #ffffff;
    --backdrop: #2e2e2e;
    --map-tone: #f1f1f1;
  }
  * { box-sizing: border-box; margin: 0; padding: 0; }
  html, body { width: 1200px; height: 1200px; overflow: hidden; }
  body {
    background: var(--backdrop);
    font-family: "Open Sans", sans-serif;
    position: relative;
  }
  .card {
    position: absolute;
    left: 150px;
    width: 900px;
    height: 514px;
    overflow: hidden;
    box-shadow: 0 14px 30px rgba(0,0,0,.45);
  }
  .card--front { top: 70px; background: var(--pink); }
  .card--back { top: 616px; background: var(--paper); }

  .brand {
    position: absolute;
    display: flex;
    align-items: center;
    gap: 16px;
  }
  .brand__name {
    font-family: "Montserrat", sans-serif;
    font-weight: 700;
    letter-spacing: 4px;
  }
  .brand__dot { border-radius: 50%; flex: none; }
  .brand__rule { position: absolute; height: 2px; }

  .card--front .brand { left: 310px; top: 190px; }
  .card--front .brand__name { color: var(--paper); font-size: 58px; }
  .card--front .brand__dot { width: 70px; height: 70px; background: var(--paper); }
  .card--front .brand__rule { left: 240px; top: 286px; width: 540px; background: var(--paper); }
  .front__web {
    position: absolute;
    right: 70px;
    bottom: 60px;
    color: var(--paper);
    font-size: 24px;
  }

  .card--back .brand { right: 60px; top: 50px; }
  .card--back .brand__name { color: var(--pink); font-size: 40px; }
  .card--back .brand__dot { width: 50px; height: 50px; background: var(--pink); }
  .card--back .brand__rule { left: 380px; top: 122px; width: 460px; background: var(--grey); }

  .map {
    position: absolute;
    left: 40px;
    top: 160px;
    width: 430px;
    height: 250px;
    background: var(--map-tone);
  }
  .contact {
    position: absolute;
    left: 520px;
    top: 170px;
    color: var(--ink);
    font-size: 20px;
    line-height: 1.35;
  }
  .contact__address { margin-bottom: 16px; }
  .contact__row { display: flex; align-items: center; gap: 10px; }
  .contact__icon { width: 20px; height: 20px; flex: none; }
  .swoosh { position: absolute; left: 0; bottom: 0; width: 900px; height: 200px; }
</style>
</head>
<body>
  <section class="card card--front">
    <div class="brand">
      <span class="brand__name">VELMARIN</span>
      <span class="brand__dot"></span>
    </div>
    <div class="brand__rule"></div>
    <p class="front__web">www.velmarin-werkstatt.de</p>
  </section>

  <section class="card card--back">
    <div class="brand">
      <span class="brand__name">VELMARIN</span>
      <span class="brand__dot"></span>
    </div>
    <div class="brand__rule"></div>

    <div class="map" role="img" aria-label="Lageplan der Werkstatt mit umliegenden Straßen"></div>

    <div class="contact">
      <p class="contact__address">Velmarin GmbH<br>Lindauer Str. 17<br>80931 München</p>
      <p class="contact__row">
        <svg class="contact__icon" viewBox="0 0 20 20"><circle cx="10" cy="10" r="10" fill="#ee1a6b"/><path d="M7 5l2 3-1 1.2c.6 1.3 1.5 2.2 2.8 2.8L12 11l3 2-1 2c-4 0-8-4-8-8z" fill="#fff"/></svg>
        0160 - 47 29 38 1
      </p>
      <p class="contact__row">
        <svg class="contact__icon" viewBox="0 0 20 20"><circle cx="10" cy="10" r="10" fill="#ee1a6b"/><rect x="5" y="6.5" width="10" height="7" fill="#fff"/><path d="M5 6.5l5 4 5-4" fill="none" stroke="#ee1a6b" stroke-width="1"/></svg>
        info@velmarin-werkstatt.de
      </p>
      <p class="contact__row">
        <svg class="contact__icon" viewBox="0 0 20 20"><circle cx="10" cy="10" r="10" fill="#ee1a6b"/><circle cx="10" cy="10" r="5" fill="none" stroke="#fff" stroke-width="1.4"/><path d="M5 10h10M10 5v10" stroke="#fff" stroke-width="1.2"/></svg>
        www.velmarin-werkstatt.de
      </p>
    </div>

    <svg class="swoosh" viewBox="0 0 900 200" preserveAspectRatio="none">
      <path d="M0 150 C 250 120, 600 90, 900 10 L900 40 C 600 120, 300 150, 0 175 Z" fill="#6b6b6b"/>
      <path d="M0 175 C 300 150, 600 120, 900 40 L900 200 L0 200 Z" fill="#ee1a6b"/>
      <path d="M0 172 C 300 147, 600 117, 900 37" fill="none" stroke="#ffffff" stroke-width="3"/>
    </svg>
  </section>
</body>
</html>
```